TerraLume Business Card Design Project

We need a business card design for a new company called "TerraLume Systems". TerraLume provides 3D visualization software for subsurface oil and gas data so you can make confident downhole decisions.

Our goal is to provide easy to understand big pictures of your data so your can make confident planning decisions.

Our tagline is
SEAMLESS DATA SHARING. EFFECTIVE COLLABORATION. CONFIDENT DECISION-MAKING

Check out http://www.terralume-example.com for more ideas.

The design should promote a technology company that delivers web-based solutions focused on photo-realistic 3D graphics.

The colors from our existing logo (attached) are one option but not a requirement. The design SHOULD NOT use the existing logo.

The design should be two sided and full color. If you require any special print considerations (example: paper type, matte finish, metallic ink, etc) please provide detailed comments. Please also specify any desired details such as rounding of corners, etc.

IF YOU USE BLACK our printer states "We recommend using CMYK black (0, 0, 0, 100) or for a rich black (60, 40, 40, 100). Ensure your artwork is in CMYK mode before adjusting the black."

For design purposes you can use the following contact information

name: Harlan Pike
title: founder
phone: 555.987.6543
email: harlan@terralume-example.com

company information
TerraLume is our "branded" name
"TerraLume Systems" is our official name
www.terralume-example.com

address:
Suite 720
482 Birchmont Avenue SW
Calgary, AB, Canada
T3K 4R8

Target Market(s)

Companies spend a lot of time collecting, organizing and analyzing data but it's really hard to to get a big picture view of current and planned projects, especially in context to existing wellbores, geology and downhole equipment

TerraLume enables you to explore the big picture in an immersive, 3D environment. Our goal is to help transform you rich data into an easily understood picture, to make confident planning decisions and anticipate trouble events before the expensive execution phase.

Industry/Entity Type

Oil And Gas

Requirements
Must have
• The business card design should be sized to a standard 3.5 x 2 inches and print ready. See the attachment for a sample sized card
It MUST meet these requirements:
Exported as PDF file with two pages:
page 1: front design
page 2: back design
All Images must be 300ppi or higher (at 100%)
CMYK colour mode
0.125 inches of bleed on all sides (0.25 inches additional width and height)
0.125 inch safety margin (inside trim line)

```html
<!DOCTYPE html>
<html lang="en">
<head>
<meta charset="utf-8">
<title>TerraLume Systems – Business Card</title>
<link rel="stylesheet" href="https://fonts.googleapis.com/css2?family=Questrial&family=Montserrat:wght@800&display=swap">
<style>
  :root {
    --page: #e9e7e3;
    --lime: #8dff12;
    --black: #0a0a0a;
    --charcoal: #1b1c1d;
    --steel: #5b5e61;
    --ink: #111;
    --text-light: #d7dadd;
  }
  * { box-sizing: border-box; margin: 0; padding: 0; }
  html, body { width: 1200px; height: 741px; overflow: hidden; }
  body {
    background: var(--page);
    display: flex;
    align-items: center;
    justify-content: center;
    gap: 40px;
    font-family: "Questrial", "Century Gothic", sans-serif;
  }
  .card {
    position: relative;
    width: 560px;
    height: 320px;
    overflow: hidden;
    box-shadow: 0 10px 28px rgba(0,0,0,.22);
  }

  /* Front */
  .card-front {
    background:
      radial-gradient(ellipse 260px 150px at 50% 30%, #4a4d50 0%, #202224 55%, transparent 100%),
      linear-gradient(180deg, var(--charcoal) 0%, var(--black) 100%);
  }
  .front-band {
    position: absolute;
    left: 0; right: 0;
    top: 158px;
    height: 26px;
    background: linear-gradient(180deg, #3a3c3e 0%, #242628 100%);
    border-top: 1px solid var(--steel);
    border-bottom: 1px solid #000;
  }
  .front-lower {
    position: absolute;
    left: 0; right: 0; top: 185px; bottom: 0;
    background: linear-gradient(180deg, #161718 0%, #050505 100%);
  }
  .tagline {
    position: absolute;
    left: 0; right: 0;
    top: 164px;
    text-align: center;
    font-size: 9.5px;
    letter-spacing: 1.6px;
    color: var(--text-light);
    text-transform: uppercase;
  }
  .front-wordmark {
    position: absolute;
    left: 0; right: 0;
    top: 192px;
    text-align: center;
    font-size: 60px;
    font-weight: 400;
    line-height: 1;
    color: var(--lime);
    letter-spacing: 1px;
  }

  /* Back */
  .card-back { background: var(--lime); }
  .back-band {
    position: absolute;
    left: 0; right: 0;
    top: 122px;
    height: 104px;
    background: var(--black);
  }
  .person {
    position: absolute;
    left: 26px;
    top: 72px;
    color: var(--ink);
  }
  .person-name {
    font-family: "Montserrat", "Verdana", sans-serif;
    font-weight: 800;
    font-size: 25px;
    line-height: 1;
  }
  .person-title {
    font-family: "Montserrat", "Verdana", sans-serif;
    font-weight: 800;
    font-size: 11px;
    margin: 3px 0 0 86px;
  }
  .contact {
    position: absolute;
    top: 134px;
    right: 22px;
    display: flex;
    gap: 22px;
    color: var(--lime);
    font-size: 11.5px;
    line-height: 1.45;
  }
  .contact address { font-style: normal; }
  .back-wordmark {
    position: absolute;
    left: 24px;
    bottom: 20px;
    display: flex;
    align-items: center;
    gap: 8px;
    font-size: 26px;
    color: var(--steel);
  }
  .back-wordmark .mark-square {
    width: 16px; height: 16px;
    background: var(--steel);
  }
</style>
</head>
<body>

  <section class="card card-front" aria-label="Card front">
    <div class="front-lower"></div>
    <div class="front-band"></div>
    <p class="tagline">Unified project data. Stronger teamwork. Smarter well planning</p>
    <h1 class="front-wordmark">TerraLume</h1>
  </section>

  <section class="card card-back" aria-label="Card back">
    <div class="back-band"></div>
    <div class="person">
      <p class="person-name">Harlan Pike</p>
      <p class="person-title">Founder</p>
    </div>
    <div class="contact">
      <p>harlan@terralume-example.com<br>www.terralume-example.com<br>(555)987-6543</p>
      <address>Suite 720 482 Birchmont Avenue<br>SW Calgary, AB,<br>Canada T3K 4R8</address>
    </div>
    <div class="back-wordmark">
      <span class="mark-square"></span>
      <span>TerraLume</span>
    </div>
  </section>

</body>
</html>
```